Professional and creatice Life Coach - Business Card design

I just relaunched my website and now i a need a correspoonding business card for my task as life coach. My website is www.tbalrond.com as reference. The compass is kind of a symbol for my work, as I help people navigate through their challenging phases in life. The business card should be colorful, but not too playful as I also adress business people. So it sould be creative, but professional (also to suport my other business as Management Consultant)

Target Market(s)

People who want to get teir problems resolved, in business, partnership and other personal realms

Industry/Entity Type

Life Coaching

Contact Information for Business Card

Front side should include Name, Phone number, Email, Website and address

Font styles to use
Sans Serif

Colors
add136

Requirements
Must have
• "Mag. Leopold Brantner" -> Name
"Energetische Praxis" -> Jobtitle (describing my profession as life coach)
colours and style should match my website www.tbalrond.com
Nice to have
• a compass as a symbol

```html
<!DOCTYPE html>
<html lang="de">
<head>
<meta charset="utf-8">
<title>Leopold Brantner – Visitenkarte</title>
<link rel="stylesheet" href="https://fonts.googleapis.com/css2?family=Overlock:wght@400;700&display=swap">
<style>
  :root {
    --lime: #add136;
    --lime-soft: #e9f2c4;
    --lime-faint: #f3f8e0;
    --charcoal: #4a4a4c;
    --ink: #333335;
    --text: #3b3b3d;
    --paper: #fdfdfd;
    --white: #ffffff;
  }
  * { box-sizing: border-box; margin: 0; padding: 0; }
  html, body {
    width: 1028px; height: 1200px; overflow: hidden;
    background: var(--white);
    font-family: "Overlock", "Trebuchet MS", sans-serif;
  }
  .canvas { position: relative; width: 1028px; height: 1200px; }
  .card {
    position: absolute; left: 35px; width: 959px; height: 549px; overflow: hidden;
  }
  .card--back { top: 35px; background: var(--charcoal); }
  .card--front { top: 617px; background: var(--paper); }

  .deco-ring { position: absolute; border-radius: 50%; }
  .card--back .deco-ring {
    left: 573px; top: 162px; width: 360px; height: 360px;
    border: 2px solid rgba(173, 209, 54, 0.28);
    background: rgba(173, 209, 54, 0.12);
  }
  .card--front .deco-ring {
    left: 563px; top: 153px; width: 380px; height: 380px;
    background: var(--lime-faint);
    border: 2px solid var(--lime-soft);
  }

  .wordmark {
    position: absolute; display: flex; align-items: center; gap: 14px;
    transform: translate(-50%, -50%);
    font-size: 34px; font-weight: 700; letter-spacing: 0.5px; white-space: nowrap;
  }
  .wordmark__dot { width: 30px; height: 30px; border-radius: 50%; }
  .card--back .wordmark { left: 470px; top: 274px; color: var(--white); }
  .card--back .wordmark__dot { background: var(--white); }
  .card--front .wordmark { left: 239px; top: 274px; color: var(--ink); }
  .card--front .wordmark__dot { background: var(--lime); }

  .web-line {
    position: absolute; left: 326px; top: 476px;
    display: flex; align-items: center; gap: 20px;
    font-size: 30px; color: var(--white); letter-spacing: 0.5px;
  }
  .web-line .accent { color: var(--lime); }
  .icon { width: 34px; height: 34px; flex: none; }

  .accent-rule {
    position: absolute; left: 411px; top: 118px; width: 4px; height: 74px;
  }
  .identity { position: absolute; left: 447px; top: 108px; }
  .identity__name { font-size: 42px; color: var(--lime); font-weight: 400; line-height: 1.1; }
  .identity__role { font-size: 33px; color: var(--text); line-height: 1.2; margin-top: 0; }
  .address {
    position: absolute; left: 447px; top: 222px;
    font-size: 31px; color: var(--text); line-height: 1.18; font-style: normal;
  }
  .contacts { position: absolute; left: 446px; top: 316px; list-style: none; }
  .contacts li {
    display: flex; align-items: center; gap: 20px;
    font-size: 31px; color: var(--text); height: 52px; letter-spacing: 0.8px;
  }
  .footer-bands { position: absolute; left: 0; bottom: 0; width: 959px; height: 34px; }
</style>
</head>
<body>
<main class="canvas">

  <section class="card card--back" aria-label="Rückseite">
    <div class="deco-ring" aria-hidden="true"></div>
    <div class="wordmark"><span class="wordmark__dot"></span>Tbalrond</div>
    <p class="web-line">
      <svg class="icon" viewBox="0 0 34 34" aria-hidden="true" fill="none" stroke="#add136" stroke-width="2">
        <circle cx="17" cy="17" r="15"/><ellipse cx="17" cy="17" rx="7" ry="15"/>
        <line x1="2" y1="17" x2="32" y2="17"/><path d="M5 9h24M5 25h24"/>
      </svg>
      <span>www.<span class="accent">tbalrond</span>.com</span>
    </p>
  </section>

  <section class="card card--front" aria-label="Vorderseite">
    <div class="deco-ring" aria-hidden="true"></div>
    <div class="wordmark"><span class="wordmark__dot"></span>Tbalrond</div>

    <svg class="accent-rule" viewBox="0 0 4 74" aria-hidden="true">
      <path d="M2 0 L4 37 L2 74 L0 37 Z" fill="#add136"/>
    </svg>
    <header class="identity">
      <h1 class="identity__name">Mag. Leopold Brantner</h1>
      <p class="identity__role">Energetische Praxis</p>
    </header>
    <address class="address">Lindenweg 14, 5020 Salzburg,<br>Österreich</address>

    <ul class="contacts">
      <li>
        <svg class="icon" viewBox="0 0 34 34" aria-hidden="true">
          <path fill="#add136" d="M8 3c2-1 4 0 5 2l3 6c1 2 0 3-1 4l-2 2c1 3 4 6 7 7l2-2c1-1 2-2 4-1l6 3c2 1 3 3 2 5l-2 3c-2 2-6 2-10 0C14 28 6 20 3 12 1 8 2 5 4 4z"/>
        </svg>
        +43 664 3817462
      </li>
      <li>
        <svg class="icon" viewBox="0 0 34 34" aria-hidden="true">
          <rect x="2" y="7" width="30" height="20" fill="#add136"/>
          <path d="M2 7 L17 19 L32 7 M2 27 L13 16 M32 27 L21 16" stroke="#fdfdfd" stroke-width="2" fill="none"/>
        </svg>
        leopold@tbalrond.com
      </li>
      <li>
        <svg class="icon" viewBox="0 0 34 34" aria-hidden="true" fill="none" stroke="#add136" stroke-width="2">
          <circle cx="17" cy="17" r="15"/><ellipse cx="17" cy="17" rx="7" ry="15"/>
          <line x1="2" y1="17" x2="32" y2="17"/><path d="M5 9h24M5 25h24"/>
        </svg>
        www.tbalrond.com
      </li>
    </ul>

    <svg class="footer-bands" viewBox="0 0 959 34" aria-hidden="true">
      <polygon points="0,0 404,0 390,34 0,34" fill="#add136"/>
      <polygon points="413,0 959,0 959,34 399,34" fill="#333335"/>
    </svg>
  </section>

</main>
</body>
</html>
```